Medical consulting firm needs polished website

I am a physician and working on setting up a smal consulting firm in New Hampshire, USA. It is called Clearpath Health Advisors, LLC and the website will be ClearpathHealthAdv.com. I was puttering around at making my own website, and it just didn't come together nicely so I've decided to leave it to the pros. The focus of the business is Advanced Care Planning, ie planning for your future medical needs. So it deals with some heavy stuff like planning for if you get sick, who should make decisions for you, end of life options etc. So it can't be too flippant or cutesy, but also can't be too dour and dark. I am hoping to convey that by thinking ahead and making some plans you can lift some of the worries off of yourself and your family - and that we can help make a scary sounding path more manageable. I want it to be made with wordpress and I have actually already bought a template ( Curova – A Bright Comprehensive Clinical & Wellness Theme ). The website needs to have general information about our services, doc profile, appointment maker, blog/url link page, and ideally web commerce application ( the template has access to woocommerce). I've posted my business card and current brochure (still tweaking them, but you get the idea). I am also partnering with lifeledgerhub.com and so have included their logo and would want connections/info about them. I have the logos etc in different formats as needed.

Target Market(s)

middle aged to older adults

Industry/Entity Type

Medical

Coding

Coded - Design and coding required

Font styles to use
Sans Serif

Requirements
Must have
• as above.
Nice to have
• Ease of reading/access for elderly viewers. woo commerce.

```html
<!DOCTYPE html>
<html lang="en">
<head>
<meta charset="utf-8">
<title>Clearpath Health Advisors</title>
<link rel="stylesheet" href="https://fonts.googleapis.com/css2?family=Open+Sans:wght@300;400;600;700&display=swap">
<style>
:root{
  --blue:#2f8fdc;
  --blue-band:#3a93db;
  --green:#3bb54a;
  --ink:#2a2a2a;
  --text:#8a8f96;
  --line:#e6e8eb;
  --hero-bg:#dcebf6;
  --footer:#2c394b;
  --footer-deep:#243041;
  --footer-text:#a7b1bf;
  --white:#fff;
}
*{box-sizing:border-box;margin:0;padding:0}
html,body{width:1200px;height:3930px;overflow:hidden}
body{font-family:"Open Sans",Arial,sans-serif;color:var(--ink);background:var(--white);position:relative}
svg{display:block}
.ph{display:block}

/* top bar */
.topbar{height:90px;display:flex;align-items:center;padding:0 100px;gap:0}
.brand{display:flex;align-items:center;gap:12px;width:260px}
.brand-dot{width:44px;height:44px;border-radius:50%;background:var(--blue)}
.brand-name{font-size:20px;font-weight:600;color:var(--blue);line-height:1.1;width:180px}
.top-info{display:flex;align-items:center;gap:12px;margin-left:60px}
.top-info + .top-info{margin-left:70px}
.top-info strong{display:block;font-size:13px;font-weight:600;color:var(--ink)}
.top-info span{font-size:12px;color:var(--text)}

/* nav */
.nav{height:50px;border-top:1px solid var(--line);border-bottom:1px solid var(--line);display:flex;align-items:center;padding:0 100px}
.nav a{font-size:12px;font-weight:600;color:var(--ink);text-decoration:none;margin-right:44px}
.lang{font-size:11px;color:var(--text);margin-left:10px;display:flex;align-items:center;gap:6px}
.flag{width:16px;height:10px;background:#c94b4b;display:inline-block}
.search{margin-left:36px}
.book{margin-left:auto;height:50px;width:210px;background:var(--green);color:var(--white);font-size:13px;font-weight:600;display:flex;align-items:center;justify-content:center;gap:10px}

/* hero */
.hero{height:432px;background:linear-gradient(90deg,#c9dbe8 0%,var(--hero-bg) 45%,#eef5fb 100%);position:relative}
.hero-photo{position:absolute;left:105px;top:0;width:360px;height:432px;background:linear-gradient(180deg,#b9ccd9,#8fa9bf)}
.hero-copy{position:absolute;left:640px;top:125px;width:470px}
.hero-title{font-size:27px;font-weight:600;color:var(--blue);letter-spacing:.3px}
.hero-sub{font-size:19px;font-weight:700;color:#3a3f45;margin-top:10px}
.hero-text{font-size:15px;line-height:1.6;color:#4d5560;margin-top:12px}
.btn-green{display:inline-block;background:var(--green);color:var(--white);font-size:13px;font-weight:700;padding:14px 26px;margin-top:18px}
.dots{position:absolute;left:578px;bottom:10px;display:flex;gap:6px}
.dots i{width:7px;height:7px;border-radius:50%;background:#9fbcd3}
.dots i:first-child{background:var(--blue)}

/* features */
.features{position:relative;margin:0 100px;height:214px;background:var(--white);box-shadow:0 4px 14px rgba(0,0,0,.08);display:flex;padding:26px 22px}
.feature{flex:1;display:flex;gap:16px;padding-right:20px}
.feature small{display:block;font-size:14px;color:var(--blue)}
.feature h3{font-size:14px;font-weight:700;margin-top:2px}
.feature p{font-size:12px;line-height:1.7;color:var(--text);margin-top:10px}

/* services */
.section-head{text-align:center}
.eyebrow{font-size:16px;color:var(--blue);margin-top:8px}
.h2{font-size:22px;font-weight:700;letter-spacing:.6px;margin-top:14px}
.rule{width:56px;height:3px;background:var(--blue);margin:18px auto 0}
.services{display:grid;grid-template-columns:repeat(3,314px);column-gap:29px;row-gap:49px;padding:52px 100px 0}
.service .ph{height:239px}
.service h4{font-size:13px;font-weight:400;margin-top:29px;color:#3a3f45}
.service a{display:flex;align-items:center;gap:6px;font-size:11px;color:var(--blue);text-decoration:none;margin-top:6px}

/* tweet band */
.band{height:336px;background:var(--blue-band);margin-top:131px;text-align:center;color:var(--white);padding-top:100px}
.band-mark{width:30px;height:30px;border-radius:50%;background:var(--white);margin:0 auto}
.band p{font-size:19px;margin-top:28px;line-height:1.7}
.band span{display:block;font-size:13px;opacity:.75;margin-top:22px}

/* future */
.future{height:450px;position:relative}
.future-photo{position:absolute;left:40px;top:30px;width:667px;height:405px;background:radial-gradient(ellipse at center,#e7d3b8 0%,#f2e9dc 45%,var(--white) 72%)}
.future-copy{position:absolute;left:733px;top:172px;width:380px}
.future-copy h2{font-size:22px;font-weight:700}
.future-copy h3{font-size:15px;font-weight:600;line-height:1.6;margin-top:12px}
.future-copy p{font-size:12px;line-height:1.8;color:var(--text);margin-top:16px}

/* news */
.news-head{text-align:center;padding-top:60px}
.news-head h2{font-size:22px;font-weight:700}
.news-head p{font-size:14px;line-height:1.8;color:#5d646d;width:760px;margin:14px auto 0}
.posts{display:grid;grid-template-columns:repeat(3,314px);column-gap:29px;padding:40px 100px 0}
.post .ph{height:233px}
.date{display:inline-block;background:var(--blue);color:var(--white);font-size:11px;padding:6px 10px;margin-top:26px}
.post h3{font-size:15px;font-weight:700;line-height:1.75;margin-top:14px}
.post p{font-size:12px;line-height:1.75;color:var(--text);margin-top:10px}
.author{display:flex;align-items:center;gap:10px;font-size:11px;color:var(--text);margin-top:22px}
.avatar{width:32px;height:32px;border-radius:50%;background:#d8c2ae}

/* help form */
.help{text-align:center;padding-top:82px}
.help h2{font-size:22px;font-weight:700}
.help p{font-size:14px;color:#5d646d;margin-top:14px}
.form{display:flex;justify-content:center;gap:14px;margin-top:28px}
.field{width:320px;height:47px;border:1px solid var(--line);font-size:12px;color:var(--text);text-align:left;padding:15px 12px}
.send{width:132px;height:47px;background:var(--green);color:var(--white);font-size:13px;font-weight:700;display:flex;align-items:center;justify-content:center}

/* footer */
.footer{position:absolute;left:0;top:3435px;width:1200px;height:430px;background:var(--footer);display:flex;padding:60px 100px 0}
.fcol{color:var(--footer-text);font-size:12px;line-height:1.7}
.fcol h4{font-size:15px;color:var(--white);font-weight:700;margin-bottom:22px;letter-spacing:.3px}
.flogo{display:flex;align-items:center;gap:12px;margin-bottom:22px}
.flogo i{width:28px;height:28px;border-radius:50%;background:var(--white)}
.flogo b{font-size:26px;color:var(--white);font-weight:600}
.fline{display:flex;gap:14px;align-items:flex-start;margin-top:22px}
.tweet{display:flex;gap:12px;margin-bottom:22px}
.tweet i{flex:none;width:14px;height:14px;border-radius:50%;background:var(--blue);margin-top:3px}
.tweet a{color:var(--white);text-decoration:none}
.rpost{display:flex;gap:16px;margin-bottom:24px}
.rpost .ph{flex:none;width:72px;height:72px;border-radius:50%}
.bottom{position:absolute;left:0;top:3865px;width:1200px;height:65px;background:var(--footer-deep);display:flex;align-items:center;padding:0 100px;font-size:11px;color:var(--footer-text)}
.social{margin-left:auto;display:flex;align-items:center;gap:8px}
.social i{width:28px;height:28px;border-radius:50%;background:#566378}
.social span{margin-right:8px}
</style>
</head>
<body>

<header class="topbar">
  <div class="brand"><span class="brand-dot"></span><span class="brand-name">Clearpath Health Advisors</span></div>
  <div class="top-info">
    <svg width="26" height="26" viewBox="0 0 26 26" fill="none" stroke="#2f8fdc" stroke-width="2"><circle cx="13" cy="13" r="10"/><path d="M13 7v6l4 3"/></svg>
    <div><strong>Monday - Friday 08:00 - 20:00</strong><span>Saturday and Sunday - CLOSED</span></div>
  </div>
  <div class="top-info">
    <svg width="26" height="26" viewBox="0 0 26 26" fill="none" stroke="#2f8fdc" stroke-width="2"><path d="M6 3h5l2 6-3 2a13 13 0 0 0 5 5l2-3 6 2v5a2 2 0 0 1-2 2A19 19 0 0 1 4 5a2 2 0 0 1 2-2z"/></svg>
    <div><strong>Call Us : 603-555-0142</strong><span>24 Hours support</span></div>
  </div>
  <div class="top-info">
    <svg width="28" height="22" viewBox="0 0 28 22" fill="none" stroke="#2f8fdc" stroke-width="2"><rect x="2" y="2" width="24" height="18"/><path d="M2 3l12 10 12-10"/></svg>
    <div><strong>info@clearpathhealthadv.com</strong><span>Reply within a hour</span></div>
  </div>
</header>

<nav class="nav">
  <a>HOME</a><a>ABOUT US</a><a>SERVICES</a><a>BLOG</a><a>TESTIMONIALS</a><a>CONTACT US</a>
  <span class="lang"><span class="flag"></span>ENGLISH ▾</span>
  <svg class="search" width="14" height="14" viewBox="0 0 14 14" fill="none" stroke="#9aa0a6" stroke-width="1.6"><circle cx="6" cy="6" r="4.5"/><path d="M9.5 9.5L13 13"/></svg>
  <span class="book"><svg width="18" height="18" viewBox="0 0 18 18" fill="none" stroke="#fff" stroke-width="2"><rect x="1" y="1" width="16" height="16" rx="2"/><path d="M5 9l3 3 5-6"/></svg>BOOK APPOINTMENT</span>
</nav>

<section class="hero">
  <div class="hero-photo ph" role="img" aria-label="Photo of a smiling female doctor in a white coat with medical staff behind her"></div>
  <div class="hero-copy">
    <h1 class="hero-title">CLEARPATH HEALTH ADVISORS</h1>
    <p class="hero-sub">Advanced Care Planning Specialists</p>
    <p class="hero-text">We are available to meet with you in the privacy of your own home or in our office and provide notary services.</p>
    <span class="btn-green">CONTACT HERE!</span>
  </div>
  <div class="dots"><i></i><i></i><i></i></div>
</section>

<section class="features">
  <div class="feature">
    <svg width="34" height="34" viewBox="0 0 34 34" fill="none" stroke="#2f8fdc" stroke-width="2"><circle cx="17" cy="11" r="6"/><path d="M5 32c0-7 5-12 12-12s12 5 12 12"/></svg>
    <div><small>Qualified Doctors</small><h3>WHERE PEOPLE COME FIRST</h3><p>Lorem ipsum dolor sit amet, consectetuer. Proin gravida nibh vel velit auctor aliquet. Aenean sollicitudi.</p></div>
  </div>
  <div class="feature">
    <svg width="34" height="34" viewBox="0 0 34 34" fill="none" stroke="#2f8fdc" stroke-width="2"><circle cx="17" cy="18" r="12"/><path d="M17 11v7l5 3M8 4l-4 4M26 4l4 4"/></svg>
    <div><small>24 Hour Service</small><h3>HIGHEST QUALITY CARE</h3><p>Lorem ipsum dolor sit amet, consectetuer. Proin gravida nibh vel velit auctor aliquet. Aenean sollicitudi.</p></div>
  </div>
  <div class="feature">
    <svg width="34" height="34" viewBox="0 0 34 34" fill="none" stroke="#2f8fdc" stroke-width="2"><path d="M17 29S3 21 3 11a7 7 0 0 1 14-2 7 7 0 0 1 14 2c0 10-14 18-14 18z"/><path d="M6 16h7l2-4 3 7 2-3h8"/></svg>
    <div><small>We Are Here For You</small><h3>EMERGENCY DEPARTMENT</h3><p>Lorem ipsum dolor sit amet, consectetuer. Proin gravida nibh vel velit auctor aliquet. Aenean sollicitudi.</p></div>
  </div>
</section>

<div class="section-head">
  <p class="eyebrow">Discover some amazing stories</p>
  <h2 class="h2">WE ARE DIFFERENT AND PROUD TO BE. SEE WHY.</h2>
  <div class="rule"></div>
</div>

<section class="services">
  <article class="service"><div class="ph" role="img" aria-label="Photo of a team of doctors in white coats" style="background:linear-gradient(180deg,#dfe6ec,#b9c8d4)"></div><h4>INTEGRATIVE MEDICINE</h4><a>Click here for view info <svg width="9" height="9" viewBox="0 0 9 9"><circle cx="4.5" cy="4.5" r="4.5" fill="#2f8fdc"/><path d="M3.5 2.5l2 2-2 2" stroke="#fff" fill="none"/></svg></a></article>
  <article class="service"><div class="ph" role="img" aria-label="Photo of a doctor with a digital medical interface" style="background:linear-gradient(180deg,#2b6fa8,#8ab8d9)"></div><h4>MEDICAL TREATMENT</h4><a>Click here for view info <svg width="9" height="9" viewBox="0 0 9 9"><circle cx="4.5" cy="4.5" r="4.5" fill="#2f8fdc"/><path d="M3.5 2.5l2 2-2 2" stroke="#fff" fill="none"/></svg></a></article>
  <article class="service"><div class="ph" role="img" aria-label="Photo of a medical team meeting at a table" style="background:linear-gradient(180deg,#eef1f3,#c4d0da)"></div><h4>SUPPORT PROGRAMS</h4><a>Click here for view info <svg width="9" height="9" viewBox="0 0 9 9"><circle cx="4.5" cy="4.5" r="4.5" fill="#2f8fdc"/><path d="M3.5 2.5l2 2-2 2" stroke="#fff" fill="none"/></svg></a></article>
  <article class="service"><div class="ph" role="img" aria-label="Photo of doctors reviewing notes together" style="background:linear-gradient(180deg,#d8e3ea,#a9bccb)"></div><h4>INTEGRATIVE MEDICINE</h4><a>Click here for view info <svg width="9" height="9" viewBox="0 0 9 9"><circle cx="4.5" cy="4.5" r="4.5" fill="#2f8fdc"/><path d="M3.5 2.5l2 2-2 2" stroke="#fff" fill="none"/></svg></a></article>
  <article class="service"><div class="ph" role="img" aria-label="Photo of a doctor holding a stethoscope" style="background:linear-gradient(180deg,#f3f4f6,#c9d3dc)"></div><h4>MEDICAL TREATMENT</h4><a>Click here for view info <svg width="9" height="9" viewBox="0 0 9 9"><circle cx="4.5" cy="4.5" r="4.5" fill="#2f8fdc"/><path d="M3.5 2.5l2 2-2 2" stroke="#fff" fill="none"/></svg></a></article>
  <article class="service"><div class="ph" role="img" aria-label="Photo of a smiling family of four" style="background:linear-gradient(180deg,#efe4d8,#d7b99b)"></div><h4>SUPPORT PROGRAMS</h4><a>Click here for view info <svg width="9" height="9" viewBox="0 0 9 9"><circle cx="4.5" cy="4.5" r="4.5" fill="#2f8fdc"/><path d="M3.5 2.5l2 2-2 2" stroke="#fff" fill="none"/></svg></a></article>
</section>

<section class="band">
  <div class="band-mark"></div>
  <p>Curova – A Bright Comprehensive Clinical &amp; Wellness Theme:<br>https://t.co/kq4Rv2Lm8Z</p>
  <span>@BrightlineStudio</span>
</section>

<section class="future">
  <div class="future-photo ph" role="img" aria-label="Photo of a happy family sitting together on the floor"></div>
  <div class="future-copy">
    <h2>THE FUTURE OF HEALTHCARE.</h2>
    <h3>LOREM IPSUM IS SIMPLY DUMMY TEXT OF THE PRINTING AND TYPESETTING INDUSTRY</h3>
    <p>Lorem Ipsum is simply dummy text of the printing and typesetting industry. Lorem Ipsum has been the industry's standard dummy text ever since the 1500s, when an unknown printer took a galley of type and scrambled it to make a type specimen book.</p>
    <p>It has survived not only five centuries, but also the leap into electronic typesetting, remaining essentially unchanged...</p>
  </div>
</section>

<section class="news-head">
  <h2>LATEST TIPS &amp; NEWS</h2>
  <p>Lorem Ipsum is simply dummy text of the printing and typesetting industry. Lorem Ipsum has been the industry's standard dummy text ever since the 1500s</p>
</section>

<section class="posts">
  <article class="post"><div class="ph" role="img" aria-label="Photo of children running across a park lawn" style="background:linear-gradient(180deg,#8fb66a,#4f7d3a)"></div><span class="date">JUNE 29, 2016</span><h3>LOREM IPSUM IS SIMPLY DUMMY TEXT OF THE PRINTING</h3><p>Lorem Ipsum is simply dummy text of the printing and typesetting industry. Lorem Ipsum has been the industry's standard dummy text...</p><div class="author"><span class="avatar"></span>by Dr Helena Marsh</div></article>
  <article class="post"><div class="ph" role="img" aria-label="Photo of a doctor examining a young patient" style="background:linear-gradient(180deg,#e6eef4,#b7cad8)"></div><span class="date">JUNE 29, 2016</span><h3>LOREM IPSUM IS SIMPLY DUMMY TEXT OF THE PRINTING</h3><p>Lorem Ipsum is simply dummy text of the printing and typesetting industry. Lorem Ipsum has been the industry's standard dummy text...</p><div class="author"><span class="avatar"></span>by Dr Helena Marsh</div></article>
  <article class="post"><div class="ph" role="img" aria-label="Photo of a man jogging on a forest trail" style="background:linear-gradient(180deg,#5f7350,#2f3f2a)"></div><span class="date">JUNE 30, 2016</span><h3>LOREM IPSUM IS SIMPLY DUMMY TEXT OF THE PRINTING</h3><p>Lorem Ipsum is simply dummy text of the printing and typesetting industry. Lorem Ipsum has been the industry's standard dummy text...</p><div class="author"><span class="avatar"></span>by Dr Helena Marsh</div></article>
</section>

<section class="help">
  <h2>NEED HELP FINDING THE RIGHT DOCTOR?</h2>
  <p>Get helpful information on what's important to you when choosing your kids pediatrician.</p>
  <div class="form"><div class="field">Name*</div><div class="field">Enter Email*</div><div class="send">SEND</div></div>
</section>

<footer class="footer">
  <div class="fcol" style="width:340px">
    <div class="flogo"><i></i><b>lifeledgerhub</b></div>
    <p style="width:200px">Lorem ipsum dolor sit amet, consectetuer. Proin gravida nibh vel velit auctor aliquet. Aenean sollicitudin, lorem quis bibendum auctor, nisi elit consequat ipsum.</p>
    <div class="fline"><svg width="16" height="22" viewBox="0 0 16 22" fill="none" stroke="#a7b1bf" stroke-width="1.6"><rect x="2" y="1" width="12" height="20" rx="2"/><path d="M6 18h4"/></svg><span>603-555-0142<br>info@clearpathhealthadv.com</span></div>
    <div class="fline"><svg width="16" height="22" viewBox="0 0 16 22" fill="none" stroke="#a7b1bf" stroke-width="1.6"><path d="M8 21S1 12 1 8a7 7 0 0 1 14 0c0 4-7 13-7 13z"/><circle cx="8" cy="8" r="2.5"/></svg><span>1220 Granite Street<br>Concord, NH 03301</span></div>
  </div>
  <div class="fcol" style="width:360px">
    <h4>LATEST TWEETS</h4>
    <div class="tweet"><i></i><p>Lorem ipsum dolor sit amet, consectetuer. Proin gravida <a>https://t.co/Pn7cYd3Ha1</a></p></div>
    <div class="tweet"><i></i><p>Lorem ipsum dolor sit amet, consectetuer. Proin gravida <a>https://t.co/Pn7cYd3Ha1</a></p></div>
    <div class="tweet"><i></i><p>Lorem ipsum dolor sit amet, consectetuer. Proin gravida <a>https://t.co/Pn7cYd3Ha1</a></p></div>
    <div class="tweet"><i></i><p>Lorem ipsum dolor sit amet, consectetuer. Proin gravida <a>https://t.co/Pn7cYd3Ha1</a></p></div>
  </div>
  <div class="fcol" style="width:300px">
    <h4>RECENT POSTS</h4>
    <div class="rpost"><div class="ph" role="img" aria-label="Thumbnail photo of a doctor with a patient" style="background:#7f9bb5"></div><p>Lorem Ipsum is simply dummy text of the printing and typesetting industry...</p></div>
    <div class="rpost"><div class="ph" role="img" aria-label="Thumbnail photo of a smiling nurse" style="background:#c9ab92"></div><p>Lorem Ipsum is simply dummy text of the printing and typesetting industry...</p></div>
    <div class="rpost"><div class="ph" role="img" aria-label="Thumbnail photo of a woman exercising outdoors" style="background:#7fa45c"></div><p>Lorem Ipsum is simply dummy text of the printing and typesetting industry...</p></div>
  </div>
</footer>

<div class="bottom">
  <span>Copyrights 2016, Clearpath Health Advisors, LLC. All rights reserved.</span>
  <div class="social"><span>Connect with our social network :</span><i></i><i></i><i></i><i></i><i></i></div>
</div>

</body>
</html>
```